Natural Sunscreen Label Design for a Natural Cosmetics brand

We are looking to create a label design for a Natural Sunscreen Lotion. The labels will be a stick-on label on a white background tube. Enclosed a file with the content and some ideas/references. Please feel free to explore more.

It is important that the SPF is highlighted as large text and to use colors that give the customer an impression this being a sunscreen from far away as well.
We like white and orange/amber/yellow.
Details attached
Our Logo is attached as well as the size template of the label.

```html
<!DOCTYPE html>
<html lang="en">
<head>
<meta charset="utf-8">
<title>Natural Sun Lotion – Label</title>
<link rel="stylesheet" href="https://fonts.googleapis.com/css2?family=Josefin+Sans:wght@400&family=Kaushan+Script&family=Roboto:wght@400;700&display=swap">
<style>
  :root {
    --amber: #fdc100;
    --amber-soft: #ffc20e;
    --ink: #111111;
    --grey: #555555;
    --paper: #ffffff;
  }
  * { margin: 0; padding: 0; box-sizing: border-box; }
  html, body { width: 1200px; height: 1200px; overflow: hidden; }
  body {
    background: var(--amber);
    font-family: "Roboto", Arial, sans-serif;
    color: var(--ink);
    position: relative;
  }
  .label {
    position: absolute;
    left: 325px; top: 60px;
    width: 550px; height: 1080px;
    background: var(--paper);
    box-shadow: 0 6px 18px rgba(0,0,0,0.12);
  }
  .label > * { position: absolute; }

  .brand-mark {
    left: 178px; top: 61px;
    width: 195px; height: 195px;
    background: var(--amber);
    border-radius: 0 0 22px 22px;
    display: flex; align-items: center; justify-content: center;
    text-align: center;
  }
  .brand-mark span {
    color: var(--paper);
    font-family: "Roboto", Arial, sans-serif;
    font-weight: 700;
    font-size: 22px;
    letter-spacing: 4px;
    line-height: 1.35;
  }

  .sun-icon { left: 62px; top: 252px; width: 110px; height: 110px; }

  .line-name {
    left: 205px; top: 282px;
    font-family: "Kaushan Script", cursive;
    font-size: 38px;
    color: var(--amber);
  }

  .product-title {
    left: 0; width: 550px; top: 338px;
    text-align: center;
    font-family: "Josefin Sans", sans-serif;
    font-weight: 400;
    font-size: 82px;
    line-height: 66px;
    padding-left: 36px;
  }

  .use-band {
    left: 140px; top: 486px;
    width: 272px; height: 29px;
    background: var(--amber);
    color: var(--paper);
    font-weight: 700;
    font-size: 23px;
    line-height: 29px;
    text-align: center;
    letter-spacing: 0.5px;
  }
  .use-band-pt {
    left: 0; width: 552px; top: 520px;
    text-align: center;
    font-size: 16px;
    color: var(--grey);
    letter-spacing: 0.4px;
  }

  .vegan-leaf { left: 368px; top: 588px; width: 60px; height: 50px; }
  .vegan-badge {
    left: 387px; top: 608px;
    width: 123px; height: 66px;
    background: var(--amber);
    color: var(--paper);
    font-weight: 700;
    font-size: 25px;
    line-height: 27px;
    text-align: right;
    padding: 7px 8px 0 0;
    letter-spacing: 1px;
  }

  .spf-label { left: 133px; top: 668px; font-weight: 700; font-size: 26px; }
  .spf-value {
    left: 118px; top: 690px;
    font-family: "Josefin Sans", sans-serif;
    font-size: 160px;
    line-height: 140px;
    letter-spacing: -6px;
  }
  .spf-plus { left: 250px; top: 646px; font-size: 64px; font-weight: 400; line-height: 64px; }
  .protection {
    left: 305px; top: 697px;
    font-weight: 700; font-size: 24px; line-height: 27px;
  }
  .uv-marks { left: 296px; top: 752px; width: 142px; height: 60px; }

  .claims {
    left: 0; width: 550px; top: 884px;
    text-align: center;
    font-size: 19px; line-height: 24px;
  }
  .claims-pt {
    left: 0; width: 550px; top: 930px;
    text-align: center;
    font-size: 14.5px; line-height: 18px;
    color: var(--grey);
  }
  .volume {
    left: 0; width: 550px; top: 1023px;
    text-align: center;
    font-size: 19px;
  }
</style>
</head>
<body>
  <div class="label">
    <div class="brand-mark"><span>SOLMAR<br>PORTUGAL</span></div>

    <svg class="sun-icon" viewBox="0 0 110 110" aria-hidden="true">
      <g stroke="var(--amber)" stroke-width="5" stroke-linecap="round">
        <line x1="55" y1="6" x2="55" y2="18"/><line x1="55" y1="92" x2="55" y2="104"/>
        <line x1="6" y1="55" x2="18" y2="55"/><line x1="92" y1="55" x2="104" y2="55"/>
        <line x1="20" y1="20" x2="29" y2="29"/><line x1="81" y1="81" x2="90" y2="90"/>
        <line x1="90" y1="20" x2="81" y2="29"/><line x1="29" y1="81" x2="20" y2="90"/>
        <line x1="35" y1="10" x2="39" y2="20"/><line x1="75" y1="10" x2="71" y2="20"/>
        <line x1="35" y1="100" x2="39" y2="90"/><line x1="75" y1="100" x2="71" y2="90"/>
        <line x1="10" y1="36" x2="20" y2="40"/><line x1="100" y1="36" x2="90" y2="40"/>
        <line x1="10" y1="74" x2="20" y2="70"/><line x1="100" y1="74" x2="90" y2="70"/>
      </g>
      <circle cx="55" cy="55" r="24" fill="var(--amber)"/>
    </svg>

    <div class="line-name">Brisamar</div>

    <h1 class="product-title">Natural<br>Sun Lotion</h1>

    <div class="use-band">FOR BODY AND FACE</div>
    <div class="use-band-pt">PARA CORPO E ROSTO</div>

    <svg class="vegan-leaf" viewBox="0 0 60 50" aria-hidden="true">
      <path d="M6 44 C4 26 18 14 34 16 C34 32 22 44 6 44 Z" fill="var(--amber)"/>
      <path d="M22 30 C24 14 40 4 56 6 C54 22 42 30 22 30 Z" fill="var(--amber)"/>
      <path d="M6 44 L44 14" stroke="var(--paper)" stroke-width="2"/>
    </svg>
    <div class="vegan-badge">100%<br>VEGAN</div>

    <div class="spf-label">SPF</div>
    <div class="spf-value">30</div>
    <div class="spf-plus">+</div>
    <div class="protection">Very High<br>Protection</div>

    <svg class="uv-marks" viewBox="0 0 142 60" aria-label="UVA and UVB">
      <circle cx="30" cy="29" r="27" fill="none" stroke="var(--ink)" stroke-width="2"/>
      <text x="30" y="38" text-anchor="middle" font-family="Roboto, Arial, sans-serif" font-weight="700" font-size="23">UVA</text>
      <text x="70" y="36" text-anchor="middle" font-family="Roboto, Arial, sans-serif" font-weight="700" font-size="20">&amp;</text>
      <circle cx="111" cy="29" r="27" fill="none" stroke="var(--ink)" stroke-width="2"/>
      <text x="111" y="38" text-anchor="middle" font-family="Roboto, Arial, sans-serif" font-weight="700" font-size="23">UVB</text>
    </svg>

    <p class="claims">With BIO Aloe Vera, Non-greasy,<br>Water Resistant, Safe for kids and adults</p>
    <p class="claims-pt">Com BIO Aloe Vera, não gorduroso,<br>Resistente à água, seguro para crianças e adultos</p>

    <div class="volume">℮ 100ml 3.3814 floz</div>
  </div>
</body>
</html>
```